Business Card Design

manufacturer of patented concrete washout containers.
www.slabrinsebins.com

Industry/Entity Type

Concrete

Contact Information for Business Card

Dale Whitford , President

Slab Rinse Bins Group
4185 Tallowby St.
Tallowmere Ca 95011
Tel: 916-555-2318
Mobile: 916-555-7064
Toll Free 877-5-RINSEBIN
daleW@slabrinsebins.com

www.slabrinsebins.com

```html
<!DOCTYPE html>
<html lang="en">
<head>
<meta charset="utf-8">
<title>Slab Rinse Bins Group – Business Card</title>
<link rel="stylesheet" href="https://fonts.googleapis.com/css2?family=Fira+Sans:wght@400;600&display=swap">
<style>
  :root {
    --backdrop: #dcdcdc;
    --card: #ffffff;
    --navy: #2a2a86;
    --swoosh: #3f77bd;
    --ink: #2b2b2b;
    --icon: #2e3a8c;
  }
  * { box-sizing: border-box; margin: 0; padding: 0; }
  html, body {
    width: 1200px; height: 800px; overflow: hidden;
    background: var(--backdrop);
    font-family: "Fira Sans", Arial, sans-serif;
  }
  .card {
    position: absolute; left: 180px; top: 160px;
    width: 840px; height: 480px;
    background: var(--card);
    box-shadow: 0 6px 18px rgba(0,0,0,.12);
    overflow: hidden;
  }
  .swoosh { position: absolute; inset: 0; }
  .brand {
    position: absolute; right: 48px; top: 46px;
    display: flex; align-items: center; gap: 12px;
    color: var(--navy); font-weight: 600; font-size: 19px;
  }
  .brand-dot {
    width: 30px; height: 30px; border-radius: 50%;
    background: var(--navy);
  }
  .holder { position: absolute; left: 70px; top: 208px; }
  .holder-name { color: var(--navy); font-weight: 600; font-size: 31px; line-height: 1.1; }
  .holder-title { color: var(--ink); font-size: 20px; margin-top: 4px; }
  .office-phone {
    position: absolute; left: 440px; top: 160px;
    display: flex; align-items: center; gap: 12px;
    color: var(--ink); font-size: 20px;
  }
  .contact-list {
    position: absolute; left: 70px; top: 298px;
    list-style: none; color: var(--ink); font-size: 20px;
  }
  .contact-list li { display: flex; align-items: center; gap: 14px; height: 34px; }
  .icon { width: 22px; height: 22px; flex: none; fill: var(--icon); }
  .toll-free {
    position: absolute; left: 470px; top: 282px;
    color: var(--ink); font-size: 20px;
  }
</style>
</head>
<body>
  <section class="card" aria-label="Business card">
    <svg class="swoosh" viewBox="0 0 840 480" aria-hidden="true">
      <path d="M40 478 C 520 478, 800 420, 780 110 C 880 300, 820 480, 560 480 L40 480 Z" fill="var(--swoosh)"/>
      <path d="M40 474 C 520 474, 796 416, 776 108" fill="none" stroke="var(--navy)" stroke-width="2"/>
    </svg>

    <div class="brand"><span class="brand-dot"></span>Slab Rinse Bins Group</div>

    <div class="holder">
      <h1 class="holder-name">Dale Whitford</h1>
      <p class="holder-title">President</p>
    </div>

    <div class="office-phone">
      <svg class="icon" viewBox="0 0 24 24"><path d="M6.6 10.8a15 15 0 0 0 6.6 6.6l2.2-2.2c.3-.3.7-.4 1-.2 1.1.4 2.3.6 3.6.6.6 0 1 .4 1 1V20c0 .6-.4 1-1 1C10.6 21 3 13.4 3 4c0-.6.4-1 1-1h3.5c.6 0 1 .4 1 1 0 1.3.2 2.5.6 3.6.1.3 0 .7-.2 1z"/></svg>
      <span>916-555-2318</span>
    </div>

    <ul class="contact-list">
      <li>
        <svg class="icon" viewBox="0 0 24 24"><path d="M7 1h10a2 2 0 0 1 2 2v18a2 2 0 0 1-2 2H7a2 2 0 0 1-2-2V3a2 2 0 0 1 2-2zm0 3v14h10V4z"/></svg>
        <span>916-555-7064</span>
      </li>
      <li>
        <svg class="icon" viewBox="0 0 24 24"><path d="M12 2a10 10 0 1 0 0 20 10 10 0 0 0 0-20zm6.9 6h-3a15 15 0 0 0-1.3-3.9A8 8 0 0 1 18.9 8zM12 4c.8 1.2 1.5 2.5 1.9 4h-3.8c.4-1.5 1.1-2.8 1.9-4zM4.3 14a8 8 0 0 1 0-4h3.4a16 16 0 0 0 0 4zm.8 2h3a15 15 0 0 0 1.3 3.9A8 8 0 0 1 5.1 16zm3-8h-3a8 8 0 0 1 4.3-3.9A15 15 0 0 0 8.1 8zM12 20c-.8-1.2-1.5-2.5-1.9-4h3.8c-.4 1.5-1.1 2.8-1.9 4zm2.3-6H9.7a14 14 0 0 1 0-4h4.6a14 14 0 0 1 0 4zm.3 5.9a15 15 0 0 0 1.3-3.9h3a8 8 0 0 1-4.3 3.9zm1.7-5.9a16 16 0 0 0 0-4h3.4a8 8 0 0 1 0 4z"/></svg>
        <span>www.slabrinsebins.com</span>
      </li>
      <li>
        <svg class="icon" viewBox="0 0 24 24"><path d="M3 5h18a1 1 0 0 1 1 1v12a1 1 0 0 1-1 1H3a1 1 0 0 1-1-1V6a1 1 0 0 1 1-1zm9 7.5L4 7.6V17h16V7.6z"/></svg>
        <span>daleW@slabrinsebins.com</span>
      </li>
      <li>
        <svg class="icon" viewBox="0 0 24 24"><path d="M12 2a7 7 0 0 0-7 7c0 5.3 7 13 7 13s7-7.7 7-13a7 7 0 0 0-7-7zm0 9.5a2.5 2.5 0 1 1 0-5 2.5 2.5 0 0 1 0 5z"/></svg>
        <span>4185 Tallowby St. Tallowmere Ca 95011</span>
      </li>
    </ul>

    <p class="toll-free">Toll Free : 877-5-RINSEBIN</p>
  </section>
</body>
</html>
```